Carte d'affaire bilingue

Nous avons besoin d'une carte d'affaire pour notre entreprise spécialisée en vente et achat de terrain. Nous sommes une agence immobilière et nous voulons une carte avec le recto en Français et le verso en anglais. Nous voulons une image sobre et épurée. Nous avons de la clientèle internationale et nous voulons une carte très professionnelle mais qui se démarque. Nous voulons cibler une clientèle commerciale, industrielle, contracteurs et promoteurs immobiliers.

Hi everybody, we saw all your conception and we are approching of what we like but the "WOW" is missing.

We love the little sign to specify (phone or email) but we can put them in a square to make like our logo, we love also dark gray not lite gray, we also love the stainless lines. In our logo you can see a little sign +. For us is signyfy " Always further" so if you can put many little +++++ in the conception somewhere very discret it will be appreciate. We also like a kind of round that make a magnyfying glass, because we search land we found opportunity.

Thank you

Reason: I ask different things in the last day but no one do what i am asking for. For the conception # 3016702 that we love we ask changes.

We like simplicity, urban design, corporate, international. The card must have one side in french and the other side in english. We like dark gray,silver, and a little bit of green.

Target Market(s)

Investors, developers, construction builders, etc...

Font styles to use
Serif
Sans Serif

Requirements
Must have
• logo
La mention: Agence immobilière (Francais) / Real Estate Agency (anglais)
Sous le nom: Courtier immobilier agréé (Français) / Real Estate Broker

```html
<!DOCTYPE html>
<html lang="en">
<head>
<meta charset="utf-8">
<title>Land Compass — Business Card</title>
<link rel="stylesheet" href="https://fonts.googleapis.com/css2?family=Cinzel:wght@400;600&display=swap">
<style>
  :root {
    --stage: #2b2b2d;
    --card-top: #f2a52a;
    --card-mid: #ea8c0c;
    --card-low: #f1b26a;
    --tile-light: #f6cfa0;
    --tile-deep: #e6801a;
    --ink: #1c1d2a;
    --ink-soft: #2e3045;
    --brand-green: #1f9a3d;
    --rule: #8a8a8a;
  }
  * { box-sizing: border-box; margin: 0; padding: 0; }
  html, body { width: 1200px; height: 891px; overflow: hidden; }
  body {
    background: var(--stage);
    font-family: "Cinzel", Georgia, serif;
    color: var(--ink);
    position: relative;
  }
  .card {
    position: absolute;
    top: 150px;
    width: 370px;
    height: 590px;
    border-radius: 26px;
    overflow: hidden;
    background: linear-gradient(180deg, var(--card-top) 0%, var(--card-mid) 55%, var(--card-low) 100%);
  }
  .card--front { left: 175px; }
  .card--back { left: 655px; }

  .tile-field {
    position: absolute;
    left: 0; right: 0; bottom: 0;
    height: 200px;
    background: linear-gradient(180deg, rgba(246,207,160,0) 0%, var(--tile-deep) 25%, var(--tile-light) 100%);
    opacity: .85;
  }

  .brand {
    position: absolute;
    display: flex;
    align-items: center;
    gap: 12px;
  }
  .brand__mark {
    width: 44px; height: 44px;
    background: var(--brand-green);
    flex: none;
  }
  .brand__name {
    font-weight: 400;
    color: var(--ink-soft);
    line-height: 1.05;
    letter-spacing: .5px;
  }
  .brand__tagline {
    position: absolute;
    font-size: 10px;
    letter-spacing: .8px;
    color: var(--ink-soft);
  }
  .brand__rule {
    position: absolute;
    height: 1px;
    background: var(--rule);
  }

  /* front */
  .card--front .brand { left: 34px; top: 78px; }
  .card--front .brand__name { font-size: 30px; }
  .card--front .brand__rule { left: 34px; right: 34px; top: 158px; }
  .card--front .brand__tagline { right: 34px; top: 164px; }

  /* back */
  .card--back .brand { left: 30px; top: 34px; }
  .card--back .brand__name { font-size: 28px; }
  .card--back .brand__rule { left: 30px; right: 30px; top: 112px; }
  .card--back .brand__tagline { right: 30px; top: 118px; }

  .person { position: absolute; left: 30px; top: 170px; }
  .person__name { font-size: 30px; font-weight: 600; letter-spacing: .5px; }
  .person__role { font-size: 13px; margin-top: 4px; line-height: 1.4; }

  .web { position: absolute; right: 30px; top: 262px; text-align: right; font-size: 12px; line-height: 1.5; }

  .contact { position: absolute; left: 30px; right: 30px; top: 318px; font-size: 12px; line-height: 1.7; }
</style>
</head>
<body>

<section class="card card--front" lang="fr" aria-label="Recto en français">
  <div class="brand">
    <span class="brand__mark"></span>
    <span class="brand__name">Le Repère<br>Foncier</span>
  </div>
  <div class="brand__rule"></div>
  <div class="brand__tagline">Agence immobilière</div>
  <div class="tile-field" role="img" aria-label="Mosaic of small orange squares fading toward the bottom edge"></div>
</section>

<section class="card card--back" lang="en" aria-label="English side">
  <div class="brand">
    <span class="brand__mark"></span>
    <span class="brand__name">Land<br>Compass</span>
  </div>
  <div class="brand__rule"></div>
  <div class="brand__tagline">Real Estate Agency</div>

  <div class="person">
    <h1 class="person__name">Maude Levasseur</h1>
    <p class="person__role">Real Estate Broker, D.A.<br>Vice-President</p>
  </div>

  <p class="web">m.levasseur@lcrf.com<br>www.lcrf.com</p>

  <p class="contact">
    P. 514 555 0148 &nbsp;F. 450 555 0173 &nbsp;C. 514 555 0126<br>
    TF 1 866 555 0190<br>
    27 Horizon Blvd., 2e, Laval, QC, H7T 1A1
  </p>

  <div class="tile-field" role="img" aria-label="Mosaic of small orange squares fading toward the bottom edge"></div>
</section>

</body>
</html>
```